Web Design for Solar Energy Consultancy Company

~ May 3, 2017 Update ~
As our project is rapidly progressing towards its completion, we started building up the list of designs that attracted the most of the team's attention. Additional submittals are still most welcome. Before submitting your proposal, however, we can recommend to review the concepts that received 4 stars as these are the ones that, in our opinion, most closely match the brief's requirements. Thank you!!
~ April 30, 2017 Update ~
The project deadline has been extended to attract a broader design community and to better tailor the final design to the requirements of the project.
A "light", "clean" (minimalistic), professionally looking, unique design is expected. Please, try to avoid industry cliches. Also, please use green, which became another industry cliche, with great caution. The brief provides minimum details to foster creativity. With the same notion in mind, the page content information is not provided.
Thank you for your feedback and support of the project!!
~ April 22, 2017 Update ~
Additional comments after starting receiving more designs:
- your attention to the brief's requirements will be highly appreciated. It is expected that the design is unique - standard, commonly used, images, formats and approaches do not fall under this category. There is no need to "bombard" with slightly different variations of the same design. It is expected that a conceptual (preliminary) design is submitted first, and, after it is reviewed (each design will receive a star rating and, if the star rating is greater than 3, a detailed feedback), the requested changes are implemented. We believe this will allow to approach the design process more efficiently and safe additional time to both the Designers's Community and our company. Thank you for understanding.
Clarification, please submit two variations of a design:
1) 1 page "business card" design that the company will be able to use during its startup stage;
2) the fully functional design (as per the requirements outlined below) for the company to transition to after the start-up period is over. Same design principles as developed for option 1 should be used for this variation.
Additional clarification, please note that the news block will not require images (at least during the start-up stage). It is envisioned to be a news feeder.
~ April 21, 2017 Update ~
Preliminary comments after receiving first designs:
- please try to create a unique design, using common elements wisely. Though such solar energy "attributes" as a solar panel or a bulb are very well recognized and allow quickly identify the nature of the business, they also became so common that in many cases a design may seem very similar to the one of others (Oh!, I've already seen this... effect).
- please try to introduce the company's logo unobtrusively. The size and position of the logo should clearly identify the company, but the message should be subtle, the logo should not distract from the main design. Brask's swoosh did not need to occupy have the screen.
- please use the green color with caution as it was with the company's logo. True, it is a green energy. But there is no need for the color to "scream" about it. Use the amount of green and its tone (avoid acid green) wisely.
--------------------------------------------------------------------------------
1. Main Goal
Develop a website that can represent the company to the industry stakeholders and become its "business card" during the start-up stage.
2. Secondary Goal
Develop a structure of a fully functional website that the "business card" design can eventually be transformed to staying consistent with the original design principles.
3. Key Audience
Varolu Corp. is providing consulting and technical services in the area of Solar Energy. The industry stakeholders include project developers, financial community, governmental bodies, OEMs, and competition.
4. Site Map
- HOME
• About
• Services
• Solar Energy
• News
• Contacts
• Social Media
- SERVICES*
- PROJECTS*
- FINANCE*
- TRAINING*
- SOLAR (ENERGY)*
* Maybe inactive / partially functional during the start-up stage.
5. Technical Specifications
Online brochure website during the start-up stage with a capability to be eventually transformed to a fully functional website while preserving the original design principles.
The design to be appealing, "light", professional, and with an intuitive and easy to navigate interface. Modern coding principles supporting efficiency and security to be utilized. Newest industry trends in website coding will be welcome.
The website to be designed so that it would fit well a computer, tablet, or mobile phone screen of any size. Cross-platform functionality to be taken into consideration to ensure that the website is fully functional on any platform.
Company's logo has already been designed and will be shared with the short-listed designers during the final design stage.
6. Interaction
The website will provide information about the company, our services, and projects. In addition, the industry insight, accumulated knowledge, and most recent trends are planned to be shared with stakeholders and attract and retain the audience.
Interaction with designers during the website development is envisioned to go through the following steps:
a) conceptual design - to be proposed by a designer originally. All conceptual designs will be reviewed and a feedback provided to pre-selected designers;
b) (preliminary and) final design - depending on the level of additional changes required can be broken into two steps. After discussing preliminary designs, company images will be provided to the selected finalists, who will compete with their final proposals.
7. Industry Stakeholders
- https://www.quellbrin.com/power/solar-power.- http://www.pakortavon.com/
- http://www.vellitrazo.com/about/company/
- https://www.oruxem.com/energy/index.html
8. Budget
Defined by the project.
9. Timescale
Defined by the project.
12. Additional Info
- No copy-cats, standard graphics, or cliches please!
- Additional information / clarifications will be gladly provided upon request.
- This specification may be updated throughout the project to reflect discussions with / changes proposed by the Designers community.

```html
<!DOCTYPE html>
<html lang="en">
<head>
<meta charset="utf-8">
<title>Varolu Corp. – Solar Energy</title>
<link href="https://fonts.googleapis.com/css2?family=Exo+2:wght@300;400;500;600&family=Open+Sans:wght@400;600&family=Roboto:wght@400;500&display=swap" rel="stylesheet">
<style>
:root{
  --orange:#f7941d;
  --orange-soft:#fba33a;
  --dark:#2b2b2b;
  --band:#454545;
  --footer:#2a2620;
  --text:#444;
  --muted:#777;
  --grey-bg:#efefef;
  --white:#fff;
}
*{box-sizing:border-box;margin:0;padding:0}
html,body{width:1200px;height:3696px;overflow:hidden}
body{position:relative;background:var(--white);font-family:"Open Sans",sans-serif;color:var(--text)}
.abs{position:absolute}
.heading{font-family:"Exo 2",sans-serif;font-weight:500;font-size:34px;color:#333;text-align:center;width:1200px;left:0}
.subheading{font-family:"Exo 2",sans-serif;font-weight:300;font-size:21px;color:var(--muted);text-align:center;width:1200px;left:0;letter-spacing:.5px}
.heading.on-orange,.subheading.on-orange{color:var(--white)}
.ornament{left:560px;width:80px;height:12px}

/* hero */
.hero{top:0;left:0;width:1200px;height:670px;background:linear-gradient(115deg,#6f95b9 0%,#a9c6de 28%,#cfe0ec 42%,#7fa2c2 58%,#b9c9b0 78%,#e8c25a 100%)}
.nav{left:44px;top:30px;width:1109px;height:78px;background:var(--dark)}
.nav-logo{left:0;top:0;width:252px;height:78px}
.brand{left:30px;top:0;height:78px;display:flex;align-items:center;gap:10px;font-family:"Exo 2",sans-serif;font-weight:600;font-size:30px;color:#333}
.brand-dot{width:30px;height:30px;border-radius:50%;background:var(--orange)}
.nav-item{top:0;line-height:78px;font-family:"Roboto",sans-serif;font-size:15px;color:var(--white);text-transform:uppercase;white-space:nowrap}
.nav-item.active::after{content:"";position:absolute;left:0;right:0;bottom:0;height:4px;background:var(--orange)}
.hero-title{left:44px;top:222px;font-family:"Exo 2",sans-serif;font-weight:400;font-size:64px;color:var(--orange);letter-spacing:2px}
.hero-sub{left:44px;top:298px;font-family:"Exo 2",sans-serif;font-weight:400;font-size:33px;color:#222;letter-spacing:1px}
.hero-text{left:44px;top:358px;width:490px;font-size:14px;line-height:21px;color:#111}
.btn{top:461px;height:49px;line-height:49px;text-align:center;font-family:"Roboto",sans-serif;font-size:15px;text-transform:uppercase;color:var(--white)}
.btn-primary{left:44px;width:161px;background:var(--orange)}
.btn-outline{left:222px;width:155px;border:2px solid var(--white);line-height:45px}

/* about */
.about-text{left:94px;top:800px;width:1012px;font-size:15.5px;line-height:25px;text-align:center;color:#444}
.about-text p+p{margin-top:22px}

/* solutions */
.solutions{top:1055px;left:0;width:1200px;height:579px;background:var(--grey-bg)}
.solution{top:1250px;width:340px;text-align:center}
.solution svg{width:84px;height:84px;display:block;margin:0 auto}
.solution h3{font-family:"Exo 2",sans-serif;font-weight:500;font-size:21px;color:#222;margin-top:18px}
.solution p{font-size:13.5px;line-height:20px;color:#555;margin:12px auto 0;width:290px}
.read-btn{display:inline-block;margin-top:18px;width:113px;height:36px;line-height:34px;border:1px solid var(--orange);font-size:13px;color:#444;background:var(--white)}

/* products */
.products{top:1634px;left:0;width:1200px;height:552px;background:var(--orange-soft)}
.card{top:1823px;width:260px;height:247px;background:var(--white)}
.card-image{width:260px;height:197px}
.card-caption{height:50px;line-height:50px;padding-left:14px;font-family:"Exo 2",sans-serif;font-size:17px;color:#444;background:#f3f3f3;white-space:nowrap}
.card-tag{left:70px;top:1908px;width:90px;height:30px;line-height:30px;text-align:center;background:var(--orange);color:var(--white);font-size:13px}
.pager{top:2140px;height:4px;width:42px;background:var(--white)}
.pager.current{background:#333}

/* services */
.timeline-bar{left:590px;top:2365px;width:18px;height:358px;border-radius:9px;background:#b7b7b7}
.service-circle{width:144px;height:144px;border-radius:50%;border:1px solid #bbb;background:var(--white);display:flex;align-items:center;justify-content:center}
.service-circle svg{width:64px;height:64px}
.service h4{font-family:"Exo 2",sans-serif;font-weight:500;font-size:20px;color:#222}
.service p{font-size:13.5px;line-height:19px;color:#555;margin-top:10px}
.service .more{display:block;margin-top:6px;font-size:13px;font-weight:600;color:var(--orange)}

/* quote */
.quote{top:2777px;left:0;width:1200px;height:160px;background:var(--band);text-align:center}
.quote-lead{margin-top:40px;font-family:"Exo 2",sans-serif;font-weight:600;font-size:31px;color:var(--orange)}
.quote-line{margin-top:6px;font-family:"Exo 2",sans-serif;font-weight:300;font-size:31px;color:var(--white);letter-spacing:.5px}

/* clients */
.client{top:3150px;width:170px;height:56px;display:flex;align-items:center;justify-content:center;gap:8px;font-family:"Exo 2",sans-serif;font-weight:600;font-size:18px;color:#8a8a8a;text-transform:uppercase;white-space:nowrap}
.client i{width:14px;height:14px;border-radius:50%;background:#9a9a9a;display:block}
.slider-arrow{top:3150px;width:54px;height:54px;border-radius:50%;border:1px solid #999}

/* footer */
.footer{top:3285px;left:0;width:1200px;height:411px;background:var(--footer);font-family:"Roboto",sans-serif}
.footer-brand{left:70px;top:3344px;display:flex;align-items:center;gap:10px;font-family:"Exo 2",sans-serif;font-weight:600;font-size:30px;color:#8d8d8d}
.footer-brand i{width:28px;height:28px;border-radius:50%;background:#8d8d8d;display:block}
.footer-about{left:68px;top:3425px;width:250px;font-size:13px;line-height:22px;color:#8d8d8d}
.social{top:3556px;width:44px;height:44px;border-radius:50%;border:1px solid #7a7a7a}
.footer-title{top:3358px;font-size:14px;font-weight:500;color:var(--white);text-transform:uppercase;letter-spacing:.5px}
.info-row{left:340px;width:230px;display:flex;gap:14px;font-size:13px;line-height:20px;color:#a5a5a5}
.info-row svg{flex:none;width:18px;height:18px;margin-top:2px}
.research{left:616px;top:3412px;list-style:none;font-size:13px;color:#a5a5a5}
.research li{height:41px}
.research li::before{content:"";display:inline-block;width:4px;height:4px;border-radius:50%;background:#a5a5a5;margin-right:12px;vertical-align:middle}
.news-text{left:894px;top:3428px;width:250px;font-size:13px;line-height:22px;color:#a5a5a5}
.news-input{left:894px;top:3499px;width:247px;height:32px;background:#d9d9d9;font-size:12px;color:#555;text-align:center;line-height:32px}
.news-btn{left:894px;top:3543px;width:247px;height:32px;background:#c57a12;color:var(--white);font-size:12px;font-weight:500;text-align:center;line-height:32px;text-transform:uppercase}
.footer-rule{left:68px;top:3622px;width:1072px;height:1px;background:#4a453e}
.copyright{left:68px;top:3651px;font-size:12px;color:#7a7a7a}
.foot-link{top:3651px;font-size:12px;color:#7a7a7a}
.foot-sep{top:3651px;font-size:12px;color:#555}
</style>
</head>
<body>

<!-- HERO -->
<section class="hero abs" role="img" aria-label="Sunflower in front of blue solar panels under a bright sky"></section>
<nav class="nav abs">
  <svg class="nav-logo abs" viewBox="0 0 252 78"><polygon points="0,0 222,0 252,39 222,78 0,78" fill="#fff"/></svg>
  <div class="brand abs"><span class="brand-dot"></span>Varolu Corp.</div>
  <span class="nav-item active abs" style="left:408px">Home</span>
  <span class="nav-item abs" style="left:506px">About</span>
  <span class="nav-item abs" style="left:613px">Services</span>
  <span class="nav-item abs" style="left:734px">Solar Energy</span>
  <span class="nav-item abs" style="left:899px">News</span>
  <span class="nav-item abs" style="left:996px">Contacts</span>
</nav>
<h1 class="hero-title abs">SOLAR ENERGY</h1>
<div class="hero-sub abs">DOESN'T COST THE EARTH</div>
<p class="hero-text abs">Solar Energy projects are financially feasible, socially beneficial, environmental friendly and generate value for its promoters, customers and community at large.</p>
<a class="btn btn-primary abs">Learn More</a>
<a class="btn btn-outline abs">Contact Now</a>

<!-- ABOUT -->
<h2 class="heading abs" style="top:698px">About Us</h2>
<div class="subheading abs" style="top:741px">Solar Expertise. Delivered.</div>
<svg class="ornament abs" style="top:785px" viewBox="0 0 80 12"><path d="M0 6H30L34 2 40 10 46 2 50 6H80" fill="none" stroke="#f7941d" stroke-width="1.5"/></svg>
<div class="about-text abs">
  <p>Kestrel Power located in Brightfield Park Northvale is a leading organisation in the field of manufacturing and installation of String Combiner and String Monitoring boxes for the solar industry. Our team of qualified engineers and managers has a combined experience of over 50 years and 250 MW delivery to date with a 100% success rate of both technology and commissioning.</p>
  <p>The company has developed Solar PV Plant SCADA software solutions specifically for Solar PV plants. Kestrel's team of engineers and technicians can customize our hardware and software to suit the requirements of each plant and commission each plant following installation. We have our own range of next generation PCB a first in the world.</p>
</div>

<!-- SOLUTIONS -->
<section class="solutions abs"></section>
<h2 class="heading abs" style="top:1110px">Solar Solutions</h2>
<div class="subheading abs" style="top:1150px">Engineering, Procurement, and Construction</div>
<svg class="ornament abs" style="top:1194px" viewBox="0 0 80 12"><path d="M0 6H30L34 2 40 10 46 2 50 6H80" fill="none" stroke="#f7941d" stroke-width="1.5"/></svg>

<div class="solution abs" style="left:32px">
  <svg viewBox="0 0 84 84"><path d="M10 40L42 12 74 40" fill="none" stroke="#333" stroke-width="4"/><path d="M18 34V76H66V34" fill="none" stroke="#333" stroke-width="4"/><rect x="54" y="14" width="8" height="14" fill="#333"/><rect x="34" y="50" width="16" height="26" fill="#f7941d"/><rect x="24" y="44" width="8" height="8" fill="#f7941d"/></svg>
  <h3>Residential rooftops</h3>
  <p>Solar energy can be taped in versatile situations and conditions. Therefore, "one solution fits all" does not hold in solar industry.</p>
  <span class="read-btn">Read More</span>
</div>
<div class="solution abs" style="left:397px">
  <svg viewBox="0 0 84 84"><rect x="12" y="20" width="24" height="56" fill="#333"/><rect x="36" y="8" width="22" height="68" fill="#555"/><rect x="58" y="34" width="16" height="42" fill="#f7941d"/><g fill="#fff"><rect x="17" y="28" width="5" height="6"/><rect x="26" y="28" width="5" height="6"/><rect x="17" y="42" width="5" height="6"/><rect x="26" y="42" width="5" height="6"/><rect x="42" y="16" width="4" height="6"/><rect x="49" y="16" width="4" height="6"/><rect x="42" y="30" width="4" height="6"/><rect x="49" y="30" width="4" height="6"/></g></svg>
  <h3>Commercial Rooftops</h3>
  <p>Solar energy can be taped in versatile situations and conditions. Therefore, "one solution fits all" does not hold in solar industry.</p>
  <span class="read-btn">Read More</span>
</div>
<div class="solution abs" style="left:761px">
  <svg viewBox="0 0 84 84"><path d="M30 22A12 12 0 0 1 54 22Z" fill="#f7941d"/><g stroke="#f7941d" stroke-width="3"><path d="M42 4V8M26 10L29 13M58 10L55 13M20 20H24M60 20H64"/></g><rect x="10" y="30" width="64" height="44" rx="4" fill="none" stroke="#333" stroke-width="4"/><g stroke="#333" stroke-width="3"><path d="M10 45H74M10 60H74M26 30V74M42 30V74M58 30V74"/></g><path d="M34 74V80H50V74" fill="#333"/></svg>
  <h3>MW Scale Solar Power Plants</h3>
  <p>Solar energy can be taped in versatile situations and conditions. Therefore, "one solution fits all" does not hold in solar industry.</p>
  <span class="read-btn">Read More</span>
</div>

<!-- PRODUCTS -->
<section class="products abs"></section>
<h2 class="heading on-orange abs" style="top:1674px">Solar Products</h2>
<div class="subheading on-orange abs" style="top:1717px">Engineering, Procurement, and Construction</div>
<svg class="ornament abs" style="top:1761px" viewBox="0 0 80 12"><path d="M0 6H30L34 2 40 10 46 2 50 6H80" fill="none" stroke="#fff" stroke-width="1.5"/></svg>

<div class="card abs" style="left:47px">
  <div class="card-image" role="img" aria-label="Hand holding a small model house with a seedling on green grass" style="background:linear-gradient(#5f8a3a,#2f4a1e)"></div>
  <div class="card-caption">String Combiner Box</div>
</div>
<span class="card-tag abs">Read More</span>
<div class="card abs" style="left:333px">
  <div class="card-image" role="img" aria-label="White monitoring drone resting on grass" style="background:linear-gradient(#7c8a62,#4e5a38)"></div>
  <div class="card-caption">Remote Monitoring Solutions</div>
</div>
<div class="card abs" style="left:613px">
  <div class="card-image" role="img" aria-label="Solar powered street light against a blue sky" style="background:linear-gradient(#2c6fc4,#7fb2e6)"></div>
  <div class="card-caption">Solar Street Lights</div>
</div>
<div class="card abs" style="left:897px">
  <div class="card-image" role="img" aria-label="Solar panel array beside a water pump in a dry landscape" style="background:linear-gradient(#8ab3dc,#b59a78)"></div>
  <div class="card-caption">Solar Water Pumps</div>
</div>
<span class="pager abs" style="left:530px"></span>
<span class="pager current abs" style="left:578px"></span>
<span class="pager abs" style="left:626px"></span>

<!-- SERVICES -->
<h2 class="heading abs" style="top:2226px">Solar Services</h2>
<div class="subheading abs" style="top:2272px">Solar O&amp;M and Telecom O&amp;M</div>
<svg class="ornament abs" style="top:2310px" viewBox="0 0 80 12"><path d="M0 6H30L34 2 40 10 46 2 50 6H80" fill="none" stroke="#f7941d" stroke-width="1.5"/></svg>

<div class="timeline-bar abs"></div>
<svg class="abs" style="left:608px;top:2414px" width="26" height="40" viewBox="0 0 26 40"><polygon points="0,0 26,20 0,40" fill="#b7b7b7"/></svg>
<svg class="abs" style="left:564px;top:2588px" width="26" height="40" viewBox="0 0 26 40"><polygon points="26,0 0,20 26,40" fill="#b7b7b7"/></svg>

<div class="service-circle abs" style="left:657px;top:2372px">
  <svg viewBox="0 0 64 64" fill="none" stroke="#333" stroke-width="3"><circle cx="32" cy="22" r="4" fill="#333"/><path d="M22 12A14 14 0 0 0 22 32M42 12A14 14 0 0 1 42 32M16 6A22 22 0 0 0 16 38M48 6A22 22 0 0 1 48 38"/><path d="M32 26L22 60M32 26L42 60M26 46H38"/></svg>
</div>
<div class="service-circle abs" style="left:386px;top:2550px">
  <svg viewBox="0 0 64 64" fill="none" stroke="#333" stroke-width="3"><circle cx="26" cy="26" r="8"/><path d="M26 8V14M26 38V44M8 26H14M38 26H44M13 13L17 17M35 35L39 39M13 39L17 35M35 17L39 13"/><circle cx="46" cy="46" r="6"/><path d="M46 34V38M46 54V58M34 46H38M54 46H58"/></svg>
</div>

<div class="service abs" style="left:200px;top:2390px;width:330px;text-align:right">
  <h4>O &amp; M Solar Based towers</h4>
  <p>Solar energy can be taped in versable situations and conditions. Therefore, "one solution fits all" does not hold in solar industry.</p>
  <span class="more">Read more</span>
</div>
<div class="service abs" style="left:658px;top:2590px;width:340px">
  <h4>Operations Maintence</h4>
  <p>Solar energy can be taped in versatile situations and conditions. Therefore, "one solution fits all" does not hold in solar industry.</p>
  <span class="more">Read more</span>
</div>

<!-- QUOTE -->
<section class="quote abs">
  <div class="quote-lead">Customers are no longer buying products and services.</div>
  <div class="quote-line">They are buying experiences, delivered via the product and services.</div>
</section>

<!-- CLIENTS -->
<h2 class="heading abs" style="top:2975px">Our Clients</h2>
<div class="subheading abs" style="top:3018px">Solar O&amp;M and Telecom O&amp;M</div>
<svg class="ornament abs" style="top:3057px" viewBox="0 0 80 12"><path d="M0 6H30L34 2 40 10 46 2 50 6H80" fill="none" stroke="#f7941d" stroke-width="1.5"/></svg>

<svg class="slider-arrow abs" style="left:44px" viewBox="0 0 54 54"><path d="M31 18L22 27 31 36" fill="none" stroke="#777" stroke-width="2"/></svg>
<svg class="slider-arrow abs" style="left:1097px" viewBox="0 0 54 54"><path d="M23 18L32 27 23 36" fill="none" stroke="#777" stroke-width="2"/></svg>
<div class="client abs" style="left:110px"><i></i>Marlowe</div>
<div class="client abs" style="left:309px"><i></i>Tavernly</div>
<div class="client abs" style="left:511px"><i></i>Ridgefield</div>
<div class="client abs" style="left:711px"><i></i>Pinecrest</div>
<div class="client abs" style="left:913px"><i></i>Studio Arca</div>

<!-- FOOTER -->
<footer class="footer abs"></footer>
<div class="footer-brand abs"><i></i>Varolu Corp.</div>
<p class="footer-about abs">We are Halvent, we industry factory company and provide you the best service and support comes register to receive service information</p>
<span class="social abs" style="left:62px"></span>
<span class="social abs" style="left:116px"></span>
<span class="social abs" style="left:165px"></span>
<span class="social abs" style="left:217px"></span>

<div class="footer-title abs" style="left:340px">Information</div>
<div class="info-row abs" style="top:3424px"><svg viewBox="0 0 18 18" fill="none" stroke="#a5a5a5" stroke-width="1.5"><path d="M9 17S3 10 3 7A6 6 0 0 1 15 7C15 10 9 17 9 17Z"/><circle cx="9" cy="7" r="2"/></svg><span>42 Meridian Lane - Westbrook - Northvale</span></div>
<div class="info-row abs" style="top:3490px"><svg viewBox="0 0 18 18" fill="none" stroke="#a5a5a5" stroke-width="1.5"><path d="M4 2L7 2 8 6 6 7C7 10 8 11 11 12L12 10 16 11V14C16 15 15 16 14 16 8 16 2 10 2 4 2 3 3 2 4 2Z"/></svg><span>(+10) 0123 000 789<br>(04) 555.0142.39</span></div>
<div class="info-row abs" style="top:3558px"><svg viewBox="0 0 18 18" fill="none" stroke="#a5a5a5" stroke-width="1.5"><rect x="2" y="4" width="14" height="10"/><path d="M2 4L9 10 16 4"/></svg><span>info@varolucorp.example</span></div>

<div class="footer-title abs" style="left:616px">Research</div>
<ul class="research abs">
  <li>Clean Energy</li>
  <li>Material Research</li>
  <li>Oil and Gas Industry</li>
  <li>Chemical Research</li>
</ul>

<div class="footer-title abs" style="left:894px">Newsletter</div>
<p class="news-text abs">Sign up for our newsletter and follow us on social media</p>
<div class="news-input abs">Enter your email...</div>
<div class="news-btn abs">Subscribe</div>

<div class="footer-rule abs"></div>
<div class="copyright abs">Copyright © 2008 - 2016 Lumenfold. All Rights Reserved</div>
<span class="foot-link abs" style="left:814px">Home</span>
<span class="foot-sep abs" style="left:872px">|</span>
<span class="foot-link abs" style="left:910px">Blog</span>
<span class="foot-sep abs" style="left:962px">|</span>
<span class="foot-link abs" style="left:990px">Services</span>
<span class="foot-sep abs" style="left:1064px">|</span>
<span class="foot-link abs" style="left:1092px">Project</span>

</body>
</html>
```